Non-Profit, Organic, Natural Feel, Clean & Simple Business Cards

Looking for a business card design. Has an organic, natural, new-age, clean and simple look/feel. We are a non-profit group that works with Moringa(a health plant/superfood) by spreading and sharing seeds of Moringa. A design that stands out but clean and professional. I will upload our new logo design. The font can be changed. Also I will upload some pictures of Moringa.
Our Facebook page is www.facebook.com/TulvaSproutTrust Check us out to get a feel of us.

Target Market(s)

Everyone. Movers & Shakers of The Sustainable, Natural Medicines & Cosmetics, Organic Food Farming Industry. And To The Common Person Or A Local Family.

Industry/Entity Type

Sustainability

Contact Information for Business Card

Email: TulvaSoilTrust@Brenwick.com
FB: www.Leafline.org/TulvaSproutTrust
Website: www.TulvaSproutTrust.com

Requirements
Must have
• Image/Pic/Design of Moringa Leaves. Somewhere on the card. Clean and Clear. So you could easily identify the Moringa from the Business Card. Something Alive, Living, Green Feel to the card design.
Nice to have
• A warm, friendly, professional feel to the design. A organic sustainable concept/future with Moringa is the business card impression/image we are trying to present.

```html
<!DOCTYPE html>
<html lang="en">
<head>
<meta charset="utf-8">
<title>Tulva Sprout Trust – Business Cards</title>
<link href="https://fonts.googleapis.com/css2?family=Cinzel:wght@400;600&display=swap" rel="stylesheet">
<style>
  :root {
    --backdrop: #3a3a3a;
    --card: #050505;
    --white: #f4f4f4;
    --green: #5cc531;
    --lime: #9ccb2a;
    --muted: #d8d8d8;
  }
  * { margin: 0; padding: 0; box-sizing: border-box; }
  html, body { width: 1200px; height: 900px; overflow: hidden; }
  body {
    background: var(--backdrop);
    font-family: "Cinzel", "Times New Roman", serif;
    position: relative;
  }
  .card {
    position: absolute;
    width: 660px;
    height: 378px;
    background: var(--card);
    box-shadow: 0 10px 30px rgba(0,0,0,.45);
  }
  .card--front { left: 110px; top: 60px; }
  .card--back { left: 430px; top: 462px; }

  /* front */
  .brand {
    position: absolute;
    left: 140px; top: 140px;
    display: flex; align-items: center; gap: 20px;
  }
  .brand__mark {
    width: 84px; height: 84px;
    background: var(--green);
    flex: none;
  }
  .brand__name {
    color: var(--white);
    font-weight: 400;
    line-height: 1;
  }
  .brand__name .line1 { display: block; font-size: 42px; letter-spacing: 1px; }
  .brand__name .line2 { display: block; font-size: 20px; letter-spacing: 14px; margin-top: 10px; padding-left: 4px; }

  /* back */
  .back__mark {
    position: absolute;
    left: 70px; top: 110px;
    width: 160px; height: 160px;
    background: var(--green);
  }
  .person {
    position: absolute;
    left: 270px; top: 116px;
    width: 370px;
  }
  .person__name {
    color: var(--white);
    font-size: 24px; font-weight: 600; letter-spacing: .5px;
    line-height: 1.2;
  }
  .person__role {
    color: var(--lime);
    font-size: 15px; margin-top: 2px;
  }
  .contacts {
    list-style: none;
    margin-top: 16px;
  }
  .contacts li {
    display: flex; align-items: center; gap: 9px;
    color: var(--muted);
    font-size: 13px; line-height: 26px;
    white-space: nowrap;
  }
  .contacts svg { width: 13px; height: 13px; flex: none; }
  .dot { width: 9px; height: 9px; border-radius: 50%; background: var(--lime); margin: 0 2px; flex: none; }
</style>
</head>
<body>
  <section class="card card--front">
    <div class="brand">
      <div class="brand__mark"></div>
      <div class="brand__name">
        <span class="line1">TULVA SPROUT</span>
        <span class="line2">TRUST</span>
      </div>
    </div>
  </section>

  <section class="card card--back">
    <div class="back__mark"></div>
    <div class="person">
      <div class="person__name">Owen Harlow</div>
      <div class="person__role">Electrical Contractor</div>
      <ul class="contacts">
        <li>
          <svg viewBox="0 0 16 16"><path fill="var(--lime)" d="M3 1l3 3-1.5 2a9 9 0 0 0 5.5 5.5L12 10l3 3-2 2C7 15 1 9 1 3z"/></svg>
          0391 555 0147
        </li>
        <li>
          <svg viewBox="0 0 16 16"><rect x="1" y="3" width="14" height="10" fill="none" stroke="var(--lime)" stroke-width="1.6"/><path d="M1 3l7 6 7-6" fill="none" stroke="var(--lime)" stroke-width="1.6"/></svg>
          TulvaSoilTrust@Brenwick.com
        </li>
        <li>
          <svg viewBox="0 0 16 16"><g fill="none" stroke="var(--lime)" stroke-width="1.4"><circle cx="8" cy="8" r="6.5"/><ellipse cx="8" cy="8" rx="3" ry="6.5"/><path d="M1.5 8h13"/></g></svg>
          www.TulvaSproutTrust.com
        </li>
        <li>
          <span class="dot"></span>
          www.Leafline.org/TulvaSproutTrust
        </li>
      </ul>
    </div>
  </section>
</body>
</html>
```